KelvrasMassage website required

We need a website for a mobile sports massage therapist in the United Kingdom. Specialising in pregnancy and postnatal massage, sports and remedial, deep tissue massage & Corprate Massage. Attached are some logos that we already have in various colours. The file named logo_white_background is what we normally use. Feel free to use the others at your discretion.

Requirements
Must have
• Service areas, Booking system.

```html
<!DOCTYPE html>
<html lang="en">
<head>
<meta charset="utf-8">
<title>Kelvras Massage</title>
<link href="https://fonts.googleapis.com/css2?family=Lobster&family=Roboto+Condensed:wght@400&family=Montserrat:wght@300;400;600&family=Open+Sans:wght@400;600&display=swap" rel="stylesheet">
<style>
:root{
  --blue:#2e9fe6;
  --blue-light:#43b2f0;
  --navy:#1c4a6b;
  --ink:#222;
  --text:#555;
  --pale:#e6f1f8;
  --black:#0b0b0b;
  --white:#fff;
  --line:#d6d6d6;
}
*{margin:0;padding:0;box-sizing:border-box}
html,body{width:1200px;height:3750px;overflow:hidden;background:var(--white)}
body{position:relative;font-family:'Open Sans',sans-serif;color:var(--ink)}
.abs{position:absolute}
.script{font-family:'Lobster',cursive;font-weight:400}

/* header */
.brand{left:85px;top:60px;display:flex;align-items:center;gap:10px;font-family:'Open Sans',sans-serif;font-weight:600;font-size:20px;color:var(--navy)}
.brand i{width:18px;height:18px;border-radius:50%;background:var(--blue);display:block}
.phone{left:748px;top:46px;font-size:17px;font-family:'Montserrat',sans-serif;display:flex;align-items:center;gap:6px}
.search{left:910px;top:39px;width:200px;height:36px;border:2px solid #333;border-radius:18px;font-size:14px;padding:7px 16px;color:#444}
.search svg{position:absolute;right:14px;top:9px}
.nav{left:560px;top:98px;display:flex;gap:38px;font-size:15px;font-family:'Montserrat',sans-serif}
.nav .active{color:var(--blue)}

/* hero */
.hero{left:0;top:155px;width:1200px;height:635px;background:linear-gradient(100deg,#cfd3d6 0%,#a9a29d 40%,#6f5b51 70%,#3b3330 100%)}
.hero-title{left:90px;top:290px;font-family:'Roboto Condensed',sans-serif;font-size:74px;color:var(--navy)}
.hero-sub{left:90px;top:378px;font-family:'Roboto Condensed',sans-serif;font-size:46px;color:#111}
.arrows{left:92px;top:638px;display:flex;gap:4px}
.arrows span{width:20px;height:20px;border-radius:50%;background:#333;display:block}

/* welcome */
.welcome-title{left:0;width:1200px;top:815px;text-align:center;font-size:40px;color:#111}
.welcome-title em{font-style:normal;color:var(--blue)}
.welcome-text{left:205px;width:790px;top:880px;text-align:center;font-size:13px;line-height:25px;color:#333}

.feature{top:1103px;width:316px;height:255px;background:var(--white);border:1px solid var(--line);text-align:center;padding-top:85px}
.feature.lifted{top:1100px;box-shadow:0 6px 16px rgba(0,0,0,.18);border:none}
.feature h3{font-size:20px;margin-bottom:12px}
.feature p{font-size:14px;line-height:25px;color:var(--text);padding:0 40px}
.feature .btn{position:absolute;left:99px;bottom:-17px;width:118px;height:36px;border:1px solid #999;border-radius:18px;background:var(--white);font-size:13px;line-height:34px}
.feature.lifted .btn{background:var(--blue);color:var(--white);border-color:var(--blue)}
.icon-circle{top:1040px;width:126px;height:126px;border-radius:50%;background:var(--blue);border:3px solid #1d8fd6;display:flex;align-items:center;justify-content:center}

/* services */
.services-band{left:0;top:1495px;width:1200px;height:425px;background:linear-gradient(90deg,#8ccff5,var(--blue-light) 45%,#2d9ce3)}
.services-title{left:0;width:1200px;top:1548px;text-align:center;font-size:37px;color:var(--white)}
.services-sub{left:0;width:1200px;top:1604px;text-align:center;font-size:16px;color:var(--white);font-weight:600}
.service{top:1683px;width:461px;height:412px;background:var(--white);box-shadow:0 4px 14px rgba(0,0,0,.25);text-align:center}
.service .photo{height:235px}
.service h3{font-size:21px;margin:22px 0 14px}
.service p{font-size:13px;line-height:24px;color:var(--text);padding:0 40px}

/* about */
.about-label{left:135px;top:2262px;font-size:21px;color:var(--navy)}
.about-title{left:135px;top:2303px;font-family:'Montserrat',sans-serif;font-weight:300;font-size:27px;line-height:33px;color:#111}
.about-text{left:135px;top:2378px;width:460px;font-size:15px;line-height:25px;color:#222}
.hours-label{left:135px;top:2472px;font-size:19px;color:var(--navy)}
.hours{left:135px;top:2505px;font-size:16px;line-height:32px;color:#222}
.call{left:135px;top:2585px;display:flex;gap:12px;align-items:flex-start}
.call small{display:block;font-size:12px;font-weight:600;letter-spacing:1px;color:var(--navy)}
.call b{display:block;font-size:19px;font-weight:400;color:var(--navy)}
.about-frame{left:685px;top:2258px;width:376px;height:372px;border:9px solid var(--blue)}
.about-photo{left:655px;top:2290px;width:382px;height:370px;background:linear-gradient(135deg,#e9c3a9,#c99479 55%,#8a5a43);box-shadow:0 6px 16px rgba(0,0,0,.2)}

/* news */
.news-title{left:0;width:1200px;top:2868px;text-align:center;font-size:40px;color:#111}
.news-photo{top:2975px;width:325px;height:357px;box-shadow:0 3px 10px rgba(0,0,0,.2)}
.news-card{left:438px;top:2975px;width:322px;height:357px;background:var(--white);border:3px solid var(--navy);padding:48px 30px 0}
.news-card .date{font-size:14px;margin-bottom:18px}
.news-card h3{font-family:'Montserrat',sans-serif;font-weight:400;font-size:23px;line-height:29px;margin-bottom:18px}
.news-card p{font-size:12px;line-height:22px;color:#333;margin-bottom:16px}
.news-card .more{font-size:12px}
.dots{left:542px;top:3390px;display:flex;gap:12px}
.dots span{width:30px;height:5px;background:#c7ccd0;display:block}
.dots .on{background:var(--blue)}

/* footer */
.foot-brand{left:95px;top:3565px;display:flex;align-items:center;gap:10px;font-family:'Open Sans',sans-serif;font-weight:600;font-size:20px;color:var(--white)}
.foot-brand i{width:18px;height:18px;border-radius:50%;background:var(--white);display:block}
.newsletter{left:615px;top:3590px;font-family:'Montserrat',sans-serif;font-size:16px;color:var(--white)}
.email{left:830px;top:3570px;width:280px;height:52px;border:2px solid var(--white);border-radius:26px;color:#bbb;font-size:13px;padding:15px 24px}
.email span{position:absolute;right:14px;top:13px;width:22px;height:22px;border-radius:50%;background:#ccc;color:#111;font-size:18px;line-height:21px;text-align:center;font-weight:600}
.foot-rule{left:95px;top:3665px;width:1015px;height:1px;background:#444}
.foot-nav{left:97px;top:3692px;display:flex;gap:22px;color:var(--white);font-size:13px}
.copyright{left:868px;top:3697px;color:var(--white);font-size:13px}
</style>
</head>
<body>

<!-- header -->
<div class="abs brand"><i></i>Kelvra's Massage</div>
<div class="abs phone">
  <svg width="16" height="16" viewBox="0 0 24 24"><path fill="#1c4a6b" d="M6.6 10.8a15 15 0 0 0 6.6 6.6l2.2-2.2a1 1 0 0 1 1-.25 11.4 11.4 0 0 0 3.6.57 1 1 0 0 1 1 1V20a1 1 0 0 1-1 1A17 17 0 0 1 3 4a1 1 0 0 1 1-1h3.5a1 1 0 0 1 1 1c0 1.25.2 2.45.57 3.57a1 1 0 0 1-.25 1z"/></svg>
  1-800-555-0142
</div>
<div class="abs search">Search
  <svg width="16" height="16" viewBox="0 0 24 24"><circle cx="10" cy="10" r="6.5" fill="none" stroke="#111" stroke-width="3"/><path d="M15 15l6 6" stroke="#111" stroke-width="3"/></svg>
</div>
<nav class="abs nav"><span class="active">Home</span><span>About Us</span><span>Services</span><span>Blog</span><span>Faq</span><span>Contact Us</span></nav>

<!-- hero -->
<div class="abs hero" role="img" aria-label="Therapist giving a back massage to a client lying on a treatment table"></div>
<div class="abs hero-title">Kelvras Massage</div>
<div class="abs hero-sub">Sports massage therapist</div>
<div class="abs arrows"><span></span><span></span></div>

<!-- background shapes -->
<svg class="abs" style="left:0;top:0" width="1200" height="3750" viewBox="0 0 1200 3750">
  <path d="M0 792 L0 772 Q600 650 1200 772 L1200 792Z" fill="#fff"/>
  <path d="M225 748 Q600 700 985 748" fill="none" stroke="#1c3f6e" stroke-width="5"/>
  <path d="M0 2700 Q600 2860 1200 2700 L1200 3420 L0 3420Z" fill="#e6f1f8"/>
  <path d="M0 3410 L1200 3410 L1200 3750 L0 3750Z" fill="#0b0b0b"/>
  <path d="M0 3410 Q600 3560 1200 3410Z" fill="#e6f1f8"/>
</svg>

<!-- welcome -->
<h1 class="abs welcome-title script">Welcome to <em>Kelvra's Massage</em></h1>
<p class="abs welcome-text">The point of using Lorem Ipsum is that it has a more-or-less normal distribution of letters, as opposed to using 'Content here, content here', making it look like readable English. Many desktop publishing packages and web page editors now use Lorem Ipsum as their default model text, and a search for 'lorem ipsum' will uncover many web sites still in their infancy.</p>

<div class="abs feature" style="left:105px"><h3 class="script">Postnatal Massage</h3><p>It is a long established fact that a reader will be distracted by the readable content of a page</p><div class="btn">Read more</div></div>
<div class="abs feature lifted" style="left:450px"><h3 class="script">Sports and Remedial</h3><p>It is a long established fact that a reader will be distracted by the readable content of a page</p><div class="btn">Read more</div></div>
<div class="abs feature" style="left:795px"><h3 class="script">Deep Tissue Massage</h3><p>It is a long established fact that a reader will be distracted by the readable content of a page</p><div class="btn">Read more</div></div>

<div class="abs icon-circle" style="left:200px">
  <svg width="60" height="60" viewBox="0 0 60 60" role="img" aria-label="Postnatal massage icon area"><rect x="8" y="8" width="44" height="44" rx="10" fill="none" stroke="#fff" stroke-width="3"/></svg>
</div>
<div class="abs icon-circle" style="left:545px">
  <svg width="60" height="60" viewBox="0 0 60 60" role="img" aria-label="Sports and remedial icon area"><rect x="8" y="8" width="44" height="44" rx="10" fill="none" stroke="#fff" stroke-width="3"/></svg>
</div>
<div class="abs icon-circle" style="left:890px">
  <svg width="60" height="60" viewBox="0 0 60 60" role="img" aria-label="Deep tissue massage icon area"><rect x="8" y="8" width="44" height="44" rx="10" fill="none" stroke="#fff" stroke-width="3"/></svg>
</div>

<!-- services -->
<div class="abs services-band" role="img" aria-label="Soft blue background of a massage room"></div>
<h2 class="abs services-title script">Our Services</h2>
<div class="abs services-sub">Neque porro quisquam est qui dolorem ipsum quia dolor sit amet</div>

<div class="abs service" style="left:122px">
  <div class="photo" role="img" aria-label="Sports massage on a client's back" style="background:linear-gradient(120deg,#e6b48e,#d89a76 45%,#3a86c4)"></div>
  <h3 class="script">Sports massage therapist</h3>
  <p>The point of using Lorem Ipsum is that it has a more-or-less normal distribution of letters, as opposed to using 'Content here, content here', making it look like readable English</p>
</div>
<div class="abs service" style="left:617px">
  <div class="photo" role="img" aria-label="Pregnant client relaxing during a massage" style="background:linear-gradient(120deg,#3f7ec0,#b48fd0 45%,#e8c0a6)"></div>
  <h3 class="script">Pregnancy &nbsp;massage</h3>
  <p>The point of using Lorem Ipsum is that it has a more-or-less normal distribution of letters, as opposed to using 'Content here, content here', making it look like readable English</p>
</div>

<!-- about -->
<div class="abs about-label script">About Us</div>
<h2 class="abs about-title">NEQUE PORRO QUISQUAM<br>EST QUI DOLOREM</h2>
<p class="abs about-text">The point of using Lorem Ipsum is that it has a more-or-less normal distribution of letters, as opposed to using 'Content here, content here', making it look like readable English.</p>
<div class="abs hours-label script">Hours:</div>
<div class="abs hours">Monday — Friday: 8AM — 8PM<br>Saturday — Sunday: 8AM — 6PM</div>
<div class="abs call">
  <svg width="28" height="40" viewBox="0 0 24 24"><path fill="#2e9fe6" d="M6.6 10.8a15 15 0 0 0 6.6 6.6l2.2-2.2a1 1 0 0 1 1-.25 11.4 11.4 0 0 0 3.6.57 1 1 0 0 1 1 1V20a1 1 0 0 1-1 1A17 17 0 0 1 3 4a1 1 0 0 1 1-1h3.5a1 1 0 0 1 1 1c0 1.25.2 2.45.57 3.57a1 1 0 0 1-.25 1z"/></svg>
  <div><small>CALL US NOW</small><b>(909) 555-0187</b></div>
</div>
<div class="abs about-frame"></div>
<div class="abs about-photo" role="img" aria-label="Client receiving a relaxing facial massage"></div>

<!-- news -->
<h2 class="abs news-title script">Latest News</h2>
<div class="abs news-photo" style="left:95px;background:linear-gradient(135deg,#f2eee9,#d9c3b3 50%,#5b5656)" role="img" aria-label="Therapist treating a client's knee"></div>
<article class="abs news-card">
  <div class="date">May 12, 2018</div>
  <h3>Porro quisquam est dolorem ipsum</h3>
  <p>The point of using Lorem Ipsum is that it has a more-or-less normal distribution of letters, as opposed to using 'Content here, content here', making it look like readable</p>
  <div class="more">Continue ›</div>
</article>
<div class="abs news-photo" style="left:783px;background:linear-gradient(135deg,#3a2820,#9b6a4e 50%,#e0b596)" role="img" aria-label="Client relaxing during a back massage"></div>
<div class="abs dots"><span class="on"></span><span></span><span></span></div>

<!-- footer -->
<div class="abs foot-brand"><i></i>Kelvra's Massage</div>
<div class="abs newsletter">JOIN OUR NEWSLETTER</div>
<div class="abs email">Email address<span>+</span></div>
<div class="abs foot-rule"></div>
<nav class="abs foot-nav"><span>Home</span><span>About</span><span>Services</span><span>Service Areas</span><span>Booking</span><span>Contact</span></nav>
<div class="abs copyright">Copyright © 2018. All Rights Reserved</div>

</body>
</html>
```